Valdarossi’s Artisan Pizzeria Menu Contest

I’m looking for a menu design for a new pizzeria - it’s farm to table type of restaurant - more upscale than a typical pizzeria - white washed wood interior with some industrial accents - I am looking for a creative menu layout using the attached sample menu items -
Valdarossi’s is an artisanal pizzeria with an atmosphere that will make you feel at home for any situation, first date, anniversary, business lunch, boys night out or girls night out with a menu inspired by the idea of a simple honest cooking paired with fresh – quality ingredients. Full service dining experience that is still casual but dedicated to extraordinary hospitality.
While developing the menu we have created a network of amazing farms and purveyors to supply our restaurant with fresh milled 100% California flour for our hand crafted dough, as well as sustainably farmed organic produce, meats and cheeses.
The menu includes classics like the Margherita pizza to daily seasonal specials, fresh salads to rustic small plates including moms meatball recipe to a fresh local burrata with handmade bread. Each dish reflects our passion for sourcing the freshest quality local ingredients.
To compliment the menu, Valdarossi’s serves an extensive wine list with selections focusing on Italian varietals. The cocktail program has been carefully crafted to offer something to entice ever palate and the beer list has unique selections of the world’s finest brewers.
Target Market(s)
25-45 year old men and women
Industry/Entity Type
American Restaurant
Requirements
Must have
- professional tone
Nice to have
- a balance of elegance and industrial (rustic)
Should not have
- photos or playful graphics etc..

```html
<!DOCTYPE html>
<html lang="en">
<head>
<meta charset="utf-8">
<title>Valdarossi’s Artisan Pizzeria – Menu</title>
<link href="https://fonts.googleapis.com/css2?family=Open+Sans:wght@400;500&family=Ropa+Sans&display=swap" rel="stylesheet">
<style>
  :root {
    --canvas: #ffffff;
    --paper: #ececec;
    --ink: #1f1f1f;
    --ink-soft: #333333;
    --accent: #e8474f;
    --rule: #3a3a3a;
  }
  * { box-sizing: border-box; margin: 0; padding: 0; }
  html, body { width: 1200px; height: 720px; overflow: hidden; background: var(--canvas); }
  body { position: relative; font-family: "Open Sans", Arial, sans-serif; color: var(--ink); }

  .menu-page {
    position: absolute; top: 22px; width: 490px; height: 634px;
    background: var(--paper);
  }
  .menu-page--front { left: 76px; }
  .menu-page--back { left: 641px; }

  .brand-name {
    position: absolute; left: 0; right: 0; top: 36px;
    text-align: center; font-size: 24px; font-weight: 500;
    letter-spacing: 1px; color: var(--ink);
  }

  .column-rule {
    position: absolute; top: 98px; height: 526px; width: 1px;
    background: var(--rule);
  }

  .column { position: absolute; top: 0; height: 100%; }
  .column--left { left: 10px; width: 226px; }
  .column--right { left: 252px; width: 230px; }

  .section-title {
    position: absolute; left: 0; top: var(--y);
    font-family: "Ropa Sans", "Arial Narrow", sans-serif;
    font-size: 24px; font-weight: 400; line-height: 26px; color: var(--accent);
    display: flex; align-items: flex-end;
  }
  .section-title::after {
    content: ""; display: block; width: 58px; margin-left: 8px; margin-bottom: 5px;
    border-bottom: 1px solid var(--rule);
  }
  .section-title::before {
    content: ""; position: absolute; left: 42px; bottom: -3px; width: 84px;
    border-bottom: 1px solid var(--rule);
  }

  .menu-item { position: absolute; left: 0; right: 0; top: var(--y); }
  .item-head {
    display: flex; justify-content: space-between; align-items: baseline;
    font-size: 16px; line-height: 20px; color: var(--ink);
  }
  .item-price { font-size: 17px; }
  .item-price--own-line { display: block; text-align: right; font-size: 17px; line-height: 22px; }
  .item-desc {
    margin-top: var(--gap, 0px); font-size: 10.4px; line-height: 15px; color: var(--ink-soft);
  }
  .crust-note { font-size: 10.4px; line-height: 20px; color: var(--ink-soft); }
  .crust-note em { font-style: italic; font-size: 14.5px; color: var(--ink); }

  .page-label {
    position: absolute; top: 662px; width: 200px; text-align: center;
    font-size: 35px; line-height: 44px; color: #111;
  }
  .page-label--front { left: 196px; }
  .page-label--back { left: 774px; }
</style>
</head>
<body>

<section class="menu-page menu-page--front" aria-label="Menu front">
  <div class="brand-name">Valdarossi’s</div>
  <div class="column-rule" style="left:245px"></div>

  <div class="column column--left">
    <h2 class="section-title" style="--y:95px">Appetizers</h2>

    <div class="menu-item" style="--y:135px">
      <div class="item-head"><span>Brussels</span><span class="item-price">$10.00</span></div>
      <p class="item-desc" style="--gap:1px">pan seared brussel sprouts with a drizzle of balsamic reduction and parm and bread crumbs</p>
    </div>
    <div class="menu-item" style="--y:212px">
      <div class="item-head"><span>Meatballs</span><span class="item-price">$13.00</span></div>
      <p class="item-desc" style="--gap:4px">moms meatballs handmade secret recipe for over 75 years</p>
    </div>
    <div class="menu-item" style="--y:276px">
      <div class="item-head"><span>Mussels</span><span class="item-price">$15.00</span></div>
      <p class="item-desc" style="--gap:4px">New Zealand Mussels in a tomato broth</p>
    </div>
    <div class="menu-item" style="--y:322px">
      <div class="item-head"><span>Romanesco</span><span class="item-price">$11.00</span></div>
      <p class="item-desc">flash fried romanesco served atop a spicy aioli</p>
    </div>
    <div class="menu-item" style="--y:382px">
      <div class="item-head"><span>Chicken wings</span><span class="item-price">$10.00</span></div>
      <p class="item-desc" style="--gap:4px">italian fried chicken wings with a kick</p>
    </div>
    <div class="menu-item" style="--y:434px">
      <div class="item-head"><span>Burrata</span><span class="item-price">$13.00</span></div>
      <p class="item-desc">Local burrata served with apples grapes and fresh made bread</p>
    </div>

    <h2 class="section-title" style="--y:495px">Salads</h2>

    <div class="menu-item" style="--y:535px">
      <div class="item-head"><span>Chopped Salad</span><span class="item-price">$13.00</span></div>
      <p class="item-desc">Lettuce mix with tomato, onions, peppers, pepperoni, chick peas, fresh mozz, italian herb ving</p>
    </div>
  </div>

  <div class="column column--right">
    <div class="menu-item" style="--y:105px">
      <div class="item-head"><span>Caesar Salad</span><span class="item-price">$11.00</span></div>
      <p class="item-desc" style="--gap:-3px">traditional caesar salad rich and creamy extra shaved parmesan</p>
    </div>
    <div class="menu-item" style="--y:163px">
      <div class="item-head"><span>Farm Salad</span><span class="item-price">$15.00</span></div>
      <p class="item-desc" style="--gap:-3px">seasonal farmers market salad</p>
    </div>
    <div class="menu-item" style="--y:207px">
      <div class="item-head"><span>Grilled Little Gem</span><span class="item-price">$11.00</span></div>
      <p class="item-desc">Grilled little gems with bacon, tomato, red onions and blue cheese dressing</p>
    </div>
    <div class="menu-item" style="--y:269px">
      <div class="item-head"><span>Spinach and Arugula Salad</span></div>
      <span class="item-price--own-line">$12.00</span>
      <p class="item-desc" style="--gap:2px">Spinach and argula, red pepperstossed in a lemon ving and housemade croutons</p>
    </div>

    <h2 class="section-title" style="--y:360px">Sandwiches</h2>

    <div class="menu-item" style="--y:402px">
      <div class="item-head"><span>Italian sub</span><span class="item-price">$13.00</span></div>
      <p class="item-desc" style="--gap:-2px">Prociutto, salumi, turkey, provolone, lettuce, tomato and herb aioli with spicy gardenia</p>
    </div>
    <div class="menu-item" style="--y:462px">
      <div class="item-head"><span>Turkey sandwich</span><span class="item-price">$12.00</span></div>
      <p class="item-desc" style="--gap:1px">housemade bread - turkey, cheddar cheese, butter lettuce, tomato and mustard aioli</p>
    </div>
    <div class="menu-item" style="--y:524px">
      <div class="item-head"><span>Meatball sub</span><span class="item-price">$13.00</span></div>
      <p class="item-desc" style="--gap:1px">Moms meatballs melted provolone on a housemade roll</p>
    </div>
  </div>
</section>

<section class="menu-page menu-page--back" aria-label="Menu back">
  <div class="brand-name">Valdarossi’s</div>
  <div class="column-rule" style="left:245px"></div>

  <div class="column column--left" style="left:11px; width:226px">
    <div class="menu-item" style="--y:97px">
      <div class="item-head"><span>Plantwise burger</span><span class="item-price">$14.00</span></div>
      <p class="item-desc" style="--gap:3px">Housemade bun - arugula , tomato, onion and a sundried tomato spread</p>
    </div>
    <div class="menu-item" style="--y:157px">
      <div class="item-head"><span>Chicken sandwich</span><span class="item-price">$13.00</span></div>
      <p class="item-desc" style="--gap:2px">Fried chicken or chicken breast, provolone, argula, tomato, served with a spicy aioli</p>
    </div>

    <h2 class="section-title" style="--y:214px">Pizzas</h2>

    <div class="menu-item" style="--y:250px">
      <div class="item-head"><span>Margherita</span><span class="item-price">$14.00</span></div>
      <p class="item-desc" style="--gap:1px">Classic Margherita pizza - Fresh Mozz Tomato Sauce and Basil</p>
    </div>
    <div class="menu-item" style="--y:306px">
      <div class="item-head"><span>Organic Sausage</span><span class="item-price">$16.00</span></div>
      <p class="item-desc" style="--gap:3px">Organic Sausage Housemade Red Sauce Mozz hint of fennel</p>
    </div>
    <div class="menu-item" style="--y:366px">
      <div class="item-head"><span>Pepperoni</span><span class="item-price">$16.00</span></div>
      <p class="item-desc" style="--gap:1px">Hollis Pepperoni - Housemade Red Sauce Chile flakes and Mozz</p>
    </div>
    <div class="menu-item" style="--y:425px">
      <div class="item-head"><span>Salumi and Burrata</span><span class="item-price">$17.00</span></div>
      <p class="item-desc">Salumi dried Red Sauce finished with whipped burrata</p>
    </div>
    <div class="menu-item" style="--y:478px">
      <div class="item-head"><span>Daily special</span><span class="item-price">$17.00</span></div>
    </div>
    <div class="menu-item" style="--y:506px">
      <div class="item-head"><span>Mushroom</span><span class="item-price">$15.00</span></div>
      <p class="item-desc">Shaved mushrooms with a Parmesan cream and melted onions</p>
    </div>
    <div class="menu-item" style="--y:562px">
      <div class="item-head"><span>Prosciutto and egg</span><span class="item-price">$16.00</span></div>
      <p class="item-desc" style="--gap:7px; line-height:13px">Parma Prosciutto Parmesan cream with Alpine Swiss and gruyere finished with an organic egg</p>
    </div>
  </div>

  <div class="column column--right" style="left:253px; width:224px">
    <div class="menu-item" style="--y:97px">
      <div class="item-head"><span>Quarttro Formaggi</span><span class="item-price">$15.00</span></div>
      <p class="item-desc" style="--gap:3px">Four cheese combination - mozz - fontina - parm cream and gruyere chile flakes and oregano</p>
    </div>
    <div class="menu-item" style="--y:174px">
      <div class="item-head"><span>Farmers Pizza</span><span class="item-price">$17.00</span></div>
      <p class="item-desc" style="--gap:2px">Seasonal vegatables cream sauce and a variety of cheese</p>
    </div>
    <div class="menu-item" style="--y:234px">
      <div class="item-head"><span>Keto friendly</span><span class="item-price">$17.00</span></div>
      <p class="item-desc" style="--gap:2px">Cauliflower crust, spinach and kale , parm cream sauce</p>
    </div>

    <h2 class="section-title" style="--y:297px">Crusts</h2>

    <p class="menu-item crust-note" style="--y:330px"><em>traditional</em> orginal crust you can't miss</p>

    <div class="menu-item" style="--y:360px">
      <div class="item-head"><span>Gluten free</span><span class="item-price">$3.00</span></div>
      <p class="item-desc" style="--gap:2px">best gluten friendly crust on the west coast</p>
    </div>
    <div class="menu-item" style="--y:405px">
      <div class="item-head"><span>Cauliflower</span><span class="item-price">$3.00</span></div>
      <p class="item-desc" style="--gap:-1px">Vegans have needs</p>
    </div>

    <h2 class="section-title" style="--y:451px">Dips</h2>

    <div class="menu-item" style="--y:490px">
      <div class="item-head"><span>ranch</span><span class="item-price">$1.00</span></div>
    </div>
    <div class="menu-item" style="--y:516px">
      <div class="item-head"><span>tomato sauce</span><span class="item-price">$1.00</span></div>
    </div>
    <div class="menu-item" style="--y:542px">
      <div class="item-head"><span>spicy dip</span><span class="item-price">$1.00</span></div>
    </div>
    <div class="menu-item" style="--y:570px">
      <div class="item-head"><span>blue cheese</span><span class="item-price">$1.00</span></div>
    </div>
  </div>
</section>

<p class="page-label page-label--front">Front</p>
<p class="page-label page-label--back">Back</p>

</body>
</html>
```